Brightrankkit.com Website Design

We would like to redesign brightrnkkit.com and we are looking for creative ideas. The new design should be clean and not resemble with any other existing website design.

The most important factor is that website have many banners/advertisements so the new design should be able to accommodate these banners of different size (Advertisement Friendly Design)

All Tools should be categorized under different main categories like all those tools that are related to content/writing will be shown under Content Tools ( Please find all categories and tools in attached file with the project). Right now all tools are showing randomly.

Also, Design single tool pages with sidebar, advertisement, and content placement.
ex. brightrankkit.com/plagiarism-checker/
brightrankkit.com/keyword-position/

Winning designer will also make the logo as well.

Target Market(s)

SEO Agencies, SEO executive, Article writers, Essay Writers, Plagiarism Checkers, Webmasters

Industry/Entity Type

Seo

Logo Text

Bright Rank Kit

Number of Pages Required

5+ page

Font styles to use
Serif
Sans Serif
Other font styles liked:
• Any

Colors

Designer to choose colors to be used in the design.

Requirements
Must have
• 1) Clean Design
• 2) Modern Look
• 3) Easy To Navigate
• 4) Separate Icon for every Tool
• 5) Advertisement/Banners Freindly Design
Nice to have
• Matching Logo
• WOW Factor
Should not have
• Complex Design
• No drop down menu

```html
<!DOCTYPE html>
<html lang="en">
<head>
<meta charset="utf-8">
<title>Bright Rank Kit – Grammar Checker</title>
<link href="https://fonts.googleapis.com/css2?family=Open+Sans:wght@400;600;700&family=Jost:wght@400;500;600&display=swap" rel="stylesheet">
<style>
:root{
  --red:#ed1c24;
  --red-dark:#a30d12;
  --ink:#1f1f1f;
  --text:#333;
  --muted:#666;
  --line:#e4e4e4;
  --panel-line:#ececec;
  --ad:#dcdcdc;
  --tile:#f4f4f4;
  --tray:#ebebeb;
  --white:#fff;
}
*{box-sizing:border-box;margin:0;padding:0}
html,body{width:1200px;height:2590px;overflow:hidden;background:var(--white)}
body{font-family:"Open Sans",Arial,sans-serif;color:var(--text)}
.canvas{position:relative;width:1200px;height:2590px;overflow:hidden}
.abs{position:absolute}
svg.ico{display:block}

/* header */
.site-header{position:absolute;left:0;top:0;width:1200px;height:64px;background:var(--white)}
.brand{position:absolute;left:135px;top:14px;display:flex;align-items:center;gap:10px;font-family:"Jost",sans-serif;font-weight:500;font-size:24px;color:var(--red)}
.brand-dot{width:22px;height:22px;border-radius:50%;background:var(--red)}
.main-nav{position:absolute;top:17px;left:0;width:1200px;height:30px}
.main-nav a{position:absolute;top:0;height:30px;line-height:30px;font-size:12px;font-weight:700;color:var(--ink);text-decoration:none;text-transform:uppercase;white-space:nowrap}
.main-nav a.active{border:2px solid var(--red);color:var(--red);text-align:center;line-height:26px}

/* hero */
.hero{position:absolute;left:0;top:64px;width:1200px;height:319px;background:linear-gradient(100deg,#6d6a68 0%,#8a8480 35%,#a9a29c 60%,#7a7572 100%)}
.hero-title{position:absolute;left:135px;top:82px;color:var(--white);font-family:"Jost",sans-serif;line-height:1}
.hero-title .lead{display:block;font-size:32px;font-weight:400;text-transform:uppercase}
.hero-title .strong{display:block;font-size:50px;font-weight:600;text-transform:uppercase;margin-top:4px}
.btn-browse{position:absolute;left:135px;top:192px;width:183px;height:48px;background:var(--red);color:var(--white);font-size:17px;font-weight:600;line-height:48px;text-align:center;text-transform:uppercase;box-shadow:0 3px 6px rgba(0,0,0,.3)}

/* panels */
.panel{position:absolute;border:2px solid var(--panel-line);background:var(--white)}
.ad-slot{position:absolute;background:var(--ad);color:#222;font-size:15px;text-transform:uppercase;display:flex;align-items:center;justify-content:center}

/* tool area */
.tool-title{position:absolute;left:145px;top:546px;width:582px;display:flex;justify-content:center;align-items:center;gap:8px;font-size:21px;font-weight:600;color:var(--ink);text-transform:uppercase}
.tool-title .mark{width:31px;height:31px;background:#1d2d44;color:var(--white);font-family:Georgia,serif;font-size:24px;font-weight:700;display:flex;align-items:center;justify-content:center}
.editor{position:absolute;left:145px;top:604px;width:582px;height:290px;border:2px solid var(--line)}
.editor .placeholder{position:absolute;left:26px;top:20px;font-size:14px;color:#444}
.editor-bar{position:absolute;left:0;bottom:0;width:100%;height:51px;background:var(--ad)}
.select{position:absolute;top:15px;height:26px;background:var(--white);border:1px solid #bbb;font-size:10px;line-height:24px;padding-left:6px;color:#333}
.select::after{content:"";position:absolute;right:6px;top:10px;border:4px solid transparent;border-top-color:#333}
.btn-red{position:absolute;background:var(--red);color:var(--white);font-size:10px;font-weight:600;text-align:center}
.upload-note{position:absolute;left:145px;top:919px;font-size:10px;color:#333}
.btn-upload{position:absolute;left:145px;top:941px;width:100px;height:31px;background:var(--red);color:var(--white);font-size:12px;font-weight:700;line-height:31px;text-align:center}

.browser{position:absolute;left:145px;top:1043px;width:582px;height:692px;border:2px solid var(--panel-line)}
.bar-red{position:absolute;background:var(--red);color:var(--white);font-size:13px;font-weight:700;text-transform:uppercase;padding-left:16px;display:flex;align-items:center}
.bar-red.plain{text-transform:none;font-size:14px}
.pager{position:absolute;top:6px;width:24px;height:24px;border:1.5px solid var(--white);display:flex;align-items:center;justify-content:center}
.cat-card{position:absolute;top:1105px;width:130px;height:133px;border:1px solid #e2e2e2;background:var(--white)}
.cat-card .icon{position:absolute;left:0;top:12px;width:100%;display:flex;justify-content:center}
.cat-card .label{position:absolute;left:0;bottom:0;width:100%;height:46px;background:var(--tile);font-size:11px;font-weight:600;color:#222;display:flex;align-items:center;justify-content:center;text-align:center;line-height:1.15}
.cat-card.current::after{content:"";position:absolute;left:57px;bottom:-9px;border:8px solid transparent;border-bottom:0;border-top-color:var(--tile)}
.tray{position:absolute;left:157px;top:1259px;width:558px;height:464px;background:var(--tray)}
.tool-card{position:absolute;width:124px;height:122px;background:var(--white)}
.tool-card .icon{position:absolute;left:0;top:14px;width:100%;display:flex;justify-content:center}
.tool-card .label{position:absolute;left:0;bottom:0;width:100%;height:29px;background:var(--ad);font-size:10px;font-weight:600;color:#222;display:flex;align-items:center;justify-content:center;text-align:center;line-height:1.1;padding:0 4px}
.tool-card.selected .label{background:var(--red);color:var(--white)}

/* sidebar */
.side-head{position:absolute;left:784px;width:269px;height:38px;background:var(--red);color:var(--white);font-size:13px;font-weight:700;text-transform:uppercase;padding-left:10px;display:flex;align-items:center}
.search-input{position:absolute;left:796px;top:490px;width:247px;height:38px;border:1px solid #ddd;font-size:11px;font-style:italic;color:#333;padding-left:14px;line-height:36px}
.search-btn{position:absolute;left:796px;top:539px;width:247px;height:39px;background:#000;color:var(--white);font-size:14px;font-weight:700;text-align:center;line-height:39px;text-transform:uppercase}
.popular{position:absolute;left:784px;top:867px;width:269px;list-style:none}
.popular li{position:relative;height:56.1px;display:flex;align-items:center;gap:14px;font-size:13px;color:#222;border-bottom:1px solid #e6e6e6}
.popular li.strong{font-weight:600}
.popular .pi{width:36px;height:36px;background:var(--tile);display:flex;align-items:center;justify-content:center}
.popular li.hover{border-bottom:2px solid var(--red)}
.popular li.hover .pi{background:var(--red)}
.social{position:absolute;top:2001px;width:57px;height:57px;border-radius:50%}

/* footer */
.site-footer{position:absolute;left:0;top:2189px;width:1200px;height:401px;background:var(--red);color:var(--white)}
.foot-brand{position:absolute;left:135px;top:70px;display:flex;align-items:center;gap:10px;font-family:"Jost",sans-serif;font-size:27px;font-weight:500}
.foot-brand .dot{width:26px;height:26px;border-radius:50%;background:var(--white)}
.contact-row{position:absolute;left:135px;display:flex;align-items:flex-start;gap:12px;font-size:12.5px;line-height:1.3}
.contact-row svg{flex:none;margin-top:1px}
.foot-h{position:absolute;top:78px;font-size:17px;font-weight:600}
.quick-links{position:absolute;left:520px;top:116px;list-style:none}
.quick-links li{height:41px;font-size:12.5px;display:flex;align-items:center;gap:14px}
.quick-links li::before{content:"";width:8px;height:8px;background:var(--red-dark)}
.news-text{position:absolute;left:765px;top:113px;width:310px;font-size:13px;line-height:1.5}
.news-input{position:absolute;left:765px;top:169px;width:302px;height:45px;border:2px solid var(--red-dark);font-size:14px;line-height:41px;padding-left:22px}
.news-btn{position:absolute;left:765px;top:223px;width:143px;height:48px;background:var(--red-dark);font-size:13px;font-weight:700;text-transform:uppercase;text-align:center;line-height:48px}
.foot-rule{position:absolute;left:0;top:352px;width:1200px;height:1px;background:rgba(255,255,255,.3)}
.copyright{position:absolute;left:135px;top:366px;font-size:11.5px}
.mini-social{position:absolute;top:362px;width:28px;height:28px;border-radius:50%;background:var(--white)}
</style>
</head>
<body>
<svg width="0" height="0" style="position:absolute" aria-hidden="true">
  <defs>
    <symbol id="i-docs" viewBox="0 0 24 24"><path d="M3 5h8l3 3v13H3z" fill="currentColor"/><path d="M9 2h7l4 4v12h-5V7l-3-3H9z" fill="currentColor"/></symbol>
    <symbol id="i-rewrite" viewBox="0 0 24 24"><circle cx="12" cy="12" r="11" fill="currentColor"/><rect x="7.5" y="7" width="9" height="10" fill="none" stroke="#fff" stroke-width="1.6"/><path d="M9.5 10h5M9.5 13h4" stroke="#fff" stroke-width="1.3"/></symbol>
    <symbol id="i-gram" viewBox="0 0 24 24"><rect width="24" height="24" fill="currentColor"/><path d="M6 20l6-16 6 16M8.3 14h7.4" fill="none" stroke="#fff" stroke-width="2.4"/></symbol>
    <symbol id="i-wcount" viewBox="0 0 24 24"><path d="M4 2h11l5 5v15H4z" fill="#fff" stroke="currentColor" stroke-width="1.5"/><path d="M7 11l2 7 3-5 3 5 2-7" fill="none" stroke="currentColor" stroke-width="1.8"/></symbol>
    <symbol id="i-image" viewBox="0 0 24 24"><rect x="2" y="4" width="20" height="16" fill="none" stroke="currentColor" stroke-width="2"/><path d="M4 18l5-6 4 4 3-3 4 5z" fill="currentColor"/><circle cx="16" cy="8.5" r="2" fill="currentColor"/></symbol>
    <symbol id="i-compress" viewBox="0 0 24 24"><rect x="2" y="3" width="11" height="18" fill="none" stroke="currentColor" stroke-width="2"/><path d="M5 8h5M5 12h5M5 16h5" stroke="currentColor" stroke-width="2"/><path d="M15 6h7v5h-7zM15 13h7v5h-7z" fill="currentColor"/></symbol>
    <symbol id="i-video" viewBox="0 0 24 24"><rect x="1" y="5" width="12" height="12" rx="1" fill="none" stroke="currentColor" stroke-width="2"/><path d="M4 14l3-4 3 4z" fill="currentColor"/><circle cx="17" cy="13" r="6" fill="currentColor"/></symbol>
    <symbol id="i-chart" viewBox="0 0 24 24"><path d="M2 2v20h20" fill="none" stroke="currentColor" stroke-width="2"/><path d="M5 17l5-6 4 3 6-8" fill="none" stroke="currentColor" stroke-width="2.4"/><path d="M16 5h5v5" fill="none" stroke="currentColor" stroke-width="2.4"/></symbol>
    <symbol id="i-link" viewBox="0 0 24 24"><rect x="2" y="11" width="12" height="8" rx="4" transform="rotate(-45 8 15)" fill="none" stroke="currentColor" stroke-width="2.6"/><rect x="10" y="5" width="12" height="8" rx="4" transform="rotate(-45 16 9)" fill="none" stroke="currentColor" stroke-width="2.6"/></symbol>
    <symbol id="i-hash" viewBox="0 0 24 24"><rect x="1.5" y="1.5" width="21" height="21" rx="3" fill="none" stroke="currentColor" stroke-width="2"/><path d="M9.5 5.5l-2 13M16.5 5.5l-2 13M6 9.5h13M5 14.5h13" fill="none" stroke="currentColor" stroke-width="2"/></symbol>
    <symbol id="i-case" viewBox="0 0 24 24"><path d="M2 7h19M16 2l5 5-5 5M22 17H3M8 12l-5 5 5 5" fill="none" stroke="currentColor" stroke-width="2"/></symbol>
    <symbol id="i-merge" viewBox="0 0 24 24"><path d="M5 2h14M12 2v18M4 17h5M20 17h-5M7 15l2 2-2 2M17 15l-2 2 2 2" fill="none" stroke="currentColor" stroke-width="1.6"/></symbol>
    <symbol id="i-imgtext" viewBox="0 0 36 20"><rect x="1" y="3" width="14" height="12" fill="none" stroke="currentColor" stroke-width="1.6"/><path d="M3 13l4-5 3 3 2-2 2 4z" fill="currentColor"/><path d="M17 9h5M20 7l2 2-2 2" fill="none" stroke="currentColor" stroke-width="1.4"/><path d="M24 1h8l3 3v15H24z" fill="none" stroke="currentColor" stroke-width="1.4"/></symbol>
    <symbol id="i-spell" viewBox="0 0 40 20"><path d="M1 10l3 4 6-9" fill="none" stroke="currentColor" stroke-width="2.4"/><text x="11" y="16" font-family="Open Sans,sans-serif" font-weight="700" font-style="italic" font-size="14" fill="currentColor">ABC</text></symbol>
  </defs>
</svg>

<div class="canvas">
  <header class="site-header">
    <div class="brand"><span class="brand-dot"></span>Bright Rank Kit</div>
    <nav class="main-nav">
      <a class="active" style="left:490px;width:73px">Home</a>
      <a style="left:579px">Services</a>
      <a style="left:670px">Tools</a>
      <a style="left:745px">Advertise</a>
      <a style="left:847px">Blog</a>
      <a style="left:916px">Contact</a>
      <a style="left:1009px">Login</a>
    </nav>
  </header>

  <section class="hero" role="img" aria-label="Dimmed photo of a tablet full of app tiles beside a keyboard and mouse on a desk">
    <h1 class="hero-title"><span class="lead">Largest platform for</span><span class="strong">Best SEO tools</span></h1>
    <div class="btn-browse">Browse tools</div>
  </section>

  <!-- main column -->
  <div class="panel" style="left:133px;top:423px;width:606px;height:1687px"></div>
  <div class="ad-slot" style="left:145px;top:437px;width:582px;height:71px">Advertisment</div>

  <h2 class="tool-title"><span class="mark">A</span>Grammer checker</h2>
  <div class="editor">
    <span class="placeholder">Put your text here....</span>
    <div class="editor-bar">
      <div class="select" style="left:17px;width:78px">English</div>
      <div class="select" style="left:100px;width:80px">American</div>
      <div class="btn-red" style="left:314px;top:15px;width:104px;height:28px;line-height:28px">Check Grammer</div>
      <div class="btn-red" style="left:430px;top:15px;width:135px;height:28px;line-height:28px">Deep Grammer Check</div>
    </div>
  </div>
  <p class="upload-note">Upload a document: (Supported Format: .doc, .docx, .txt)</p>
  <div class="btn-upload">Upload File</div>

  <div class="browser"></div>
  <div class="bar-red" style="left:157px;top:1057px;width:558px;height:36px">Search tools
    <span class="pager" style="left:490px"><svg width="10" height="12" viewBox="0 0 10 12"><path d="M7 1L2 6l5 5" fill="none" stroke="#fff" stroke-width="1.6"/></svg></span>
    <span class="pager" style="left:522px"><svg width="10" height="12" viewBox="0 0 10 12"><path d="M3 1l5 5-5 5" fill="none" stroke="#fff" stroke-width="1.6"/></svg></span>
  </div>

  <div class="cat-card current" style="left:157px"><div class="icon"><svg class="ico" width="62" height="62" style="color:#2a2a2a"><use href="#i-docs"/></svg></div><div class="label">Content Tools</div></div>
  <div class="cat-card" style="left:300px"><div class="icon"><svg class="ico" width="60" height="60" style="color:#2a2a2a"><use href="#i-image"/></svg></div><div class="label">Image Handling<br>Tools</div></div>
  <div class="cat-card" style="left:443px"><div class="icon"><svg class="ico" width="60" height="60" style="color:#2a2a2a"><use href="#i-chart"/></svg></div><div class="label">Keyword Tools</div></div>
  <div class="cat-card" style="left:586px"><div class="icon"><svg class="ico" width="60" height="60" style="color:#2a2a2a"><use href="#i-link"/></svg></div><div class="label">Backlink Tools</div></div>

  <div class="tray"></div>
  <div class="bar-red plain" style="left:167px;top:1272px;width:537px;height:32px">Content Tools</div>

  <div class="tool-card" style="left:169px;top:1317px"><div class="icon"><svg class="ico" width="58" height="58" style="color:#2a2a2a"><use href="#i-docs"/></svg></div><div class="label">Plagiarism Checker</div></div>
  <div class="tool-card" style="left:305px;top:1317px"><div class="icon"><svg class="ico" width="56" height="56" style="color:#2a2a2a"><use href="#i-rewrite"/></svg></div><div class="label">Article Rewriter</div></div>
  <div class="tool-card selected" style="left:441px;top:1317px"><div class="icon"><svg class="ico" width="56" height="56" style="color:var(--red)"><use href="#i-gram"/></svg></div><div class="label">Grammer Checker</div></div>
  <div class="tool-card" style="left:578px;top:1317px"><div class="icon"><svg class="ico" width="58" height="58" style="color:#2a2a2a"><use href="#i-wcount"/></svg></div><div class="label">Word Count Checker</div></div>

  <div class="tool-card" style="left:169px;top:1452px"><div class="icon"><svg class="ico" width="76" height="38" style="color:#2a2a2a;margin-top:12px"><use href="#i-spell"/></svg></div><div class="label">Spell Checker</div></div>
  <div class="tool-card" style="left:305px;top:1452px"><div class="icon"><svg class="ico" width="50" height="50" style="color:#2a2a2a;margin-top:4px"><use href="#i-hash"/></svg></div><div class="label">Online MD5<br>Generator</div></div>
  <div class="tool-card" style="left:441px;top:1452px"><div class="icon"><svg class="ico" width="56" height="56" style="color:#2a2a2a"><use href="#i-case"/></svg></div><div class="label">Change Text Case</div></div>
  <div class="tool-card" style="left:578px;top:1452px"><div class="icon"><svg class="ico" width="58" height="58" style="color:#2a2a2a"><use href="#i-merge"/></svg></div><div class="label">Merge Words Online Tool</div></div>

  <div class="tool-card" style="left:169px;top:1588px"><div class="icon"><svg class="ico" width="80" height="44" style="color:#2a2a2a;margin-top:8px"><use href="#i-imgtext"/></svg></div><div class="label">Image To Text<br>Converter</div></div>

  <!-- sidebar -->
  <div class="panel" style="left:770px;top:423px;width:298px;height:1687px"></div>
  <div class="side-head" style="top:437px">Search tools</div>
  <div class="search-input">Search from SEO Tools</div>
  <div class="search-btn">Search</div>
  <div class="ad-slot" style="left:784px;top:620px;width:269px;height:159px">Advertisment</div>
  <div class="side-head" style="top:820px;padding-left:16px">Popular tools</div>
  <ul class="popular">
    <li><span class="pi"><svg class="ico" width="26" height="26" style="color:#111"><use href="#i-docs"/></svg></span>Plagiarism Checker</li>
    <li><span class="pi"><svg class="ico" width="24" height="24" style="color:#111"><use href="#i-rewrite"/></svg></span>Article Rewriter</li>
    <li><span class="pi"><svg class="ico" width="24" height="24" style="color:#111"><use href="#i-gram"/></svg></span>Grammer Checker</li>
    <li><span class="pi"><svg class="ico" width="26" height="26" style="color:#111"><use href="#i-wcount"/></svg></span>Word Count Checker</li>
    <li class="hover"><span class="pi"><svg class="ico" width="24" height="24" style="color:#fff"><use href="#i-image"/></svg></span>Reverse Image Search
      <svg class="abs" style="left:224px;top:16px" width="28" height="32" viewBox="0 0 28 32" aria-hidden="true"><path d="M9 30V11a2 2 0 014 0v8-3a2 2 0 014 0v3-2a2 2 0 014 0v3-1a2 2 0 014 0v6c0 4-3 7-7 7h-4c-3 0-5-2-6-4l-4-6a2 2 0 013-2l2 2" fill="#fff" stroke="#222" stroke-width="1.4" stroke-linejoin="round"/></svg></li>
    <li><span class="pi"><svg class="ico" width="26" height="26" style="color:#111"><use href="#i-compress"/></svg></span>Image Compression</li>
    <li><span class="pi"><svg class="ico" width="26" height="26" style="color:#111"><use href="#i-video"/></svg></span>Video To GIF Converter</li>
    <li><span class="pi"><svg class="ico" width="26" height="26" style="color:#111"><use href="#i-docs"/></svg></span>Plagiarism Checker</li>
    <li><span class="pi"><svg class="ico" width="24" height="24" style="color:#111"><use href="#i-rewrite"/></svg></span>Article Rewriter</li>
    <li><span class="pi"><svg class="ico" width="24" height="24" style="color:#111"><use href="#i-gram"/></svg></span>Grammer Checker</li>
    <li><span class="pi"><svg class="ico" width="26" height="26" style="color:#111"><use href="#i-wcount"/></svg></span>Word Count Checker</li>
    <li><span class="pi"><svg class="ico" width="24" height="24" style="color:#111"><use href="#i-image"/></svg></span>Reverse Image Search</li>
    <li><span class="pi"><svg class="ico" width="26" height="26" style="color:#111"><use href="#i-compress"/></svg></span>Image Compression</li>
    <li><span class="pi"><svg class="ico" width="26" height="26" style="color:#111"><use href="#i-video"/></svg></span>Video To GIF Converter</li>
    <li class="strong"><span class="pi"><svg class="ico" width="24" height="24" style="color:#111"><use href="#i-chart"/></svg></span>Keyword Position</li>
  </ul>
  <div class="ad-slot" style="left:784px;top:1740px;width:269px;height:159px">Advertisment</div>
  <div class="side-head" style="top:1941px;padding-left:16px">Follow us</div>
  <span class="social" style="left:808px;background:#3b5998" aria-label="Social profile one"></span>
  <span class="social" style="left:891px;background:#4a90d9" aria-label="Social profile two"></span>
  <span class="social" style="left:973px;background:#dd3c31" aria-label="Social profile three"></span>

  <!-- footer -->
  <footer class="site-footer">
    <div class="foot-brand"><span class="dot"></span>Bright Rank Kit</div>
    <div class="contact-row" style="top:167px"><svg width="18" height="18" viewBox="0 0 18 18"><path d="M9 1v16M3 6h12" stroke="#3a0a0a" stroke-width="2.4"/></svg><span>72 Harbor Crest, Maple Row<br>Lakeview Avenue, Townfield</span></div>
    <div class="contact-row" style="top:219px"><svg width="18" height="18" viewBox="0 0 18 18"><path d="M4 1l3 4-2 2c1 3 3 5 6 6l2-2 4 3-2 3C8 17 1 10 1 3z" fill="#3a0a0a"/></svg><span>555 014 2870<br>555 019 4432</span></div>
    <div class="contact-row" style="top:285px"><svg width="18" height="14" viewBox="0 0 18 14"><rect x="1" y="1" width="16" height="12" fill="#3a0a0a"/><path d="M1 1l8 6 8-6" fill="none" stroke="#ed1c24" stroke-width="1.4"/></svg><span>info@brightrankkit.com</span></div>

    <h3 class="foot-h" style="left:520px">Quick Links</h3>
    <ul class="quick-links">
      <li>Terms of Services</li>
      <li>Testimonials</li>
      <li>Privacy Policy</li>
      <li>Contact Us</li>
    </ul>

    <h3 class="foot-h" style="left:765px">Subscribe to Our Newsletter</h3>
    <p class="news-text">Sed ut perspiciatis unde omnis iste natus error sit voluptatem accusantium doloremque</p>
    <div class="news-input">Enter Your Email</div>
    <div class="news-btn">Subscribe</div>

    <div class="foot-rule"></div>
    <p class="copyright">Copyright © 2012-2017 by Brightrankkit.com. All Rights Reserved.</p>
    <span class="mini-social" style="left:963px"></span>
    <span class="mini-social" style="left:1001px"></span>
    <span class="mini-social" style="left:1039px"></span>
  </footer>
</div>
</body>
</html>
```